New Print Material Needed for Renovation Company

We are looking to update our current Print Material to reflect the current process we offer to our clients. A lot of the information is also outdated along with many of the photos that are currently being used. We are a renovation company that specializes in residential and commercial renovations and custom builds.This project is MULTIPLE pages. We will pay the chosen designer an extra fee for the designing 3-4 additional pages that are similar to the chosen design. Attached is our current Print Material. We are hoping to update the look of them and some of the messaging. Our current company colors are white, blue and light grey and it will remain that way.

Industry/Entity Type

Construction Company

Font styles to use
Sans Serif

Colors
3176b5
ffffff

Requirements
Must have
• Easy to explain the process
• Easy to read and understand let alone
• Easy to navigate
Nice to have
• As much creativity as possible
Should not have
• no confusing text
• no confusing layout

```html
<!DOCTYPE html>
<html lang="en">
<head>
<meta charset="utf-8">
<title>Master Builder Timeline</title>
<link rel="stylesheet" href="https://fonts.googleapis.com/css2?family=Open+Sans:wght@400;700;800&display=swap">
<style>
  :root {
    --brand-blue: #1762a3;
    --brand-blue-dark: #135a97;
    --panel-tint: #dde6f2;
    --week-blue: #3d7cbf;
    --ink: #111111;
    --card-shadow: #9b9b9b;
    --white: #ffffff;
  }
  * { margin: 0; padding: 0; box-sizing: border-box; }
  html, body { width: 1200px; height: 1000px; overflow: hidden; background: var(--white); }
  body { font-family: "Open Sans", Arial, sans-serif; position: relative; }

  .sheet { position: absolute; inset: 0; overflow: hidden; }
  .sheet-frame {
    position: absolute; left: 53px; top: 57px; width: 1095px; height: 1000px;
    border: 2px solid var(--brand-blue);
  }
  .side-band {
    position: absolute; left: 1093px; top: 352px; width: 55px; height: 700px;
    background: var(--brand-blue-dark);
  }
  .phase-rail {
    position: absolute; left: 53px; top: 338px; width: 437px; height: 700px;
    background: var(--brand-blue-dark);
  }

  .page-title {
    position: absolute; left: 0; width: 1200px; top: 250px;
    text-align: center; font-weight: 800; font-size: 62px; letter-spacing: 1px;
    color: var(--ink); line-height: 84px;
  }

  .phase-label {
    position: absolute; left: 80px; width: 34px;
    color: var(--white); font-weight: 800; font-size: 38px;
    text-align: center; line-height: 46px;
  }
  .phase-label--design { top: 370px; }
  .phase-label--plan { top: 772px; line-height: 62px; }

  .phase-box {
    position: absolute; left: 137px; width: 351px;
    background: var(--panel-tint); border: 3px solid var(--brand-blue);
  }
  .phase-box--design { top: 352px; height: 341px; }
  .phase-box--plan { top: 708px; height: 360px; }

  .step {
    position: absolute; left: 150px; width: 325px;
  }
  .step-name {
    font-weight: 800; font-size: 22px; line-height: 24px;
    color: var(--brand-blue); letter-spacing: 0.3px;
  }
  .step-duration {
    position: absolute; left: 150px; font-size: 18px; font-weight: 400;
    color: var(--week-blue);
  }
  .step-note-line {
    position: absolute; left: 150px; width: 323px; height: 28px; background: var(--white);
  }

  .step-card {
    position: absolute; left: 603px; width: 480px; height: 97px;
    background: var(--white); border: 3px solid var(--brand-blue);
    box-shadow: 12px 10px 0 var(--card-shadow);
    padding: 12px 18px 0 40px;
    font-size: 21.5px; line-height: 23px; color: var(--ink);
  }

  .connectors { position: absolute; left: 0; top: 0; }
</style>
</head>
<body>
<main class="sheet">
  <div class="sheet-frame"></div>
  <div class="side-band"></div>
  <div class="phase-rail"></div>

  <svg class="connectors" width="1200" height="1000" viewBox="0 0 1200 1000" aria-hidden="true">
    <!-- badge -->
    <g transform="translate(600 158)">
      <polygon fill="var(--brand-blue)" points="
        0,-88 9,-78 20,-86 26,-74 39,-79 41,-65 55,-66 53,-52 67,-49 61,-37 74,-31 65,-21 76,-12 65,-4 74,7 63,14 69,27 56,31 59,45 45,46 44,60 31,58 26,71 14,66 6,77 -3,69 -13,77 -19,66 -31,71 -34,58 -47,60 -47,46 -60,45 -57,31 -69,27 -63,14 -74,7 -65,-4 -76,-12 -65,-21 -74,-31 -61,-37 -67,-49 -53,-52 -55,-66 -41,-65 -39,-79 -26,-74 -20,-86 -9,-78"/>
      <circle r="62" fill="none" stroke="var(--white)" stroke-width="4"/>
    </g>
    <!-- title ribbons -->
    <polygon fill="var(--brand-blue)" points="80,258 118,258 118,322 80,322 96,290"/>
    <polygon fill="var(--brand-blue)" points="1080,258 1118,258 1102,290 1118,322 1080,322"/>
  </svg>

  <h1 class="page-title">MASTER BUILDER TIMELINE</h1>

  <div class="phase-label phase-label--design">D<br>E<br>S<br>I<br>G<br>N</div>
  <div class="phase-label phase-label--plan">P<br>L<br>A<br>N</div>

  <div class="phase-box phase-box--design"></div>
  <div class="phase-box phase-box--plan"></div>

  <div class="step" style="top:364px"><p class="step-name">INITIAL DESIGN MEETING</p></div>
  <span class="step-duration" style="top:399px">1-2 WEEKS</span>
  <div class="step-note-line" style="top:420px"></div>

  <div class="step" style="top:468px"><p class="step-name">SECOND DESIGN MEETING</p></div>
  <span class="step-duration" style="top:503px">1-2 WEEKS</span>
  <div class="step-note-line" style="top:524px"></div>

  <div class="step" style="top:570px"><p class="step-name">FINAL DESIGN<br>(PLAN + SCOPE)</p></div>
  <span class="step-duration" style="top:627px">1-3 WEEKS</span>
  <div class="step-note-line" style="top:648px"></div>

  <div class="step" style="top:719px"><p class="step-name">MATERIAL SELECTION</p></div>
  <span class="step-duration" style="top:755px">1-4 WEEKS</span>
  <div class="step-note-line" style="top:776px"></div>

  <div class="step" style="top:822px"><p class="step-name">ENGINEER DRAWINGS</p></div>
  <span class="step-duration" style="top:858px">2-4 WEEKS</span>
  <div class="step-note-line" style="top:880px"></div>

  <div class="step" style="top:924px"><p class="step-name">COMPLETE BUILDING<br>PERMIT PLANS</p></div>
  <span class="step-duration" style="top:982px">3-25 WEEKS</span>

  <div class="step-card" style="top:353px">The first step of the design process is to confirm the design concept you have envisioned.</div>
  <div class="step-card" style="top:461px">Our designers work directly with you to ensure the measurements line up with your design ideas.</div>
  <div class="step-card" style="top:568px">Any last minute or final revisions will be completed within three days of this meeting.</div>
  <div class="step-card" style="top:677px">Our material selection coordinator will work with you to ensure all the right materials.</div>
  <div class="step-card" style="top:785px">The final permit drawings will be sent to engineers to ensure structural integrity.</div>
  <div class="step-card" style="top:893px">Permit drawings will begin once the build has been signed and initial payments have been made.</div>

  <svg class="connectors" width="1200" height="1000" viewBox="0 0 1200 1000" aria-hidden="true">
    <g fill="var(--panel-tint)" stroke="var(--brand-blue)" stroke-width="2.5">
      <polyline points="487,392 497,400 487,408"/>
      <polyline points="487,484 497,492 487,500"/>
      <polyline points="487,612 497,620 487,628"/>
      <polyline points="487,740 497,748 487,756"/>
      <polyline points="487,838 497,846 487,854"/>
      <polyline points="487,964 497,972 487,980"/>
    </g>
    <g fill="none" stroke="#8a8a8a" stroke-width="3.5" stroke-dasharray="1 5" stroke-linecap="round">
      <path d="M503 400 H567"/>
      <path d="M503 492 H555 V508 H567"/>
      <path d="M503 620 H545 V604 H567"/>
      <path d="M503 748 H550 V722 H567"/>
      <path d="M503 846 H545 V830 H567"/>
      <path d="M503 972 H545 V938 H567"/>
    </g>
    <g font-family="Open Sans, Arial, sans-serif" font-weight="800" font-size="34" fill="var(--white)" text-anchor="middle">
      <g transform="translate(597 400)"><circle r="33" fill="#8f8f8f"/><circle r="30" fill="var(--white)"/><circle r="27" fill="var(--brand-blue)"/><text y="12">1</text></g>
      <g transform="translate(597 508)"><circle r="33" fill="#8f8f8f"/><circle r="30" fill="var(--white)"/><circle r="27" fill="var(--brand-blue)"/><text y="12">2</text></g>
      <g transform="translate(597 614)"><circle r="33" fill="#8f8f8f"/><circle r="30" fill="var(--white)"/><circle r="27" fill="var(--brand-blue)"/><text y="12">3</text></g>
      <g transform="translate(597 722)"><circle r="33" fill="#8f8f8f"/><circle r="30" fill="var(--white)"/><circle r="27" fill="var(--brand-blue)"/><text y="12">4</text></g>
      <g transform="translate(597 830)"><circle r="33" fill="#8f8f8f"/><circle r="30" fill="var(--white)"/><circle r="27" fill="var(--brand-blue)"/><text y="12">5</text></g>
      <g transform="translate(597 938)"><circle r="33" fill="#8f8f8f"/><circle r="30" fill="var(--white)"/><circle r="27" fill="var(--brand-blue)"/><text y="12">6</text></g>
    </g>
  </svg>
</main>
</body>
</html>
```